Bright, Fun and hard to forget home inspection business card.

We need a Business card design for a new Home Inspection company. We are building a brand that is bright, fun and easy to remember.

Target Market(s)

Anyone involed in buying and selling of homes.

Industry/Entity Type

Home Inspection

Contact Information for Business Card

Colin Radford Owner/Inspector

Wedsite- PorchAndRafterCheck.example
Phone: 555-718-4062
Email- ColinRadford@mailbox.example
WA Lic # 8467

Requirements
Must have
• QBRV LOGO somewhere on card.

```html
<!DOCTYPE html>
<html lang="en">
<head>
<meta charset="utf-8">
<title>Porch &amp; Rafter Check LLC – Business Card</title>
<link rel="stylesheet" href="https://fonts.googleapis.com/css2?family=Oswald:wght@500&family=Open+Sans:wght@400;600;700&display=swap">
<style>
  :root {
    --backdrop: #e4dfd8;
    --card-black: #1d1d1d;
    --card-white: #ffffff;
    --brand-orange: #e8512a;
    --ink-dark: #242424;
    --ink-grey: #6b6b6b;
    --badge-grey: #cfcfcf;
  }
  * { box-sizing: border-box; margin: 0; padding: 0; }
  html, body {
    width: 1200px; height: 913px; overflow: hidden;
    background: var(--backdrop);
    font-family: "Open Sans", Arial, sans-serif;
  }
  .stage { position: relative; width: 1200px; height: 913px; }
  .card {
    position: absolute; top: 306px;
    width: 520px; height: 300px;
    border-radius: 22px; overflow: hidden;
    box-shadow: 0 10px 28px rgba(0,0,0,.22);
  }
  .card--front { left: 50px; background: var(--card-black); }
  .card--back { left: 630px; background: var(--card-white); }
  .card__bands { position: absolute; inset: 0; width: 520px; height: 300px; }

  .brand-mark {
    position: absolute; display: flex; align-items: center; gap: 14px;
  }
  .brand-mark__dot { width: 34px; height: 34px; border-radius: 50%; background: var(--brand-orange); flex: none; }
  .brand-mark__name {
    font-family: "Oswald", Arial, sans-serif; font-weight: 500;
    text-transform: uppercase; line-height: 1.02; letter-spacing: .5px;
    white-space: nowrap;
  }
  .card--front .brand-mark { left: 120px; top: 92px; }
  .card--front .brand-mark__name { color: #ffffff; font-size: 40px; }
  .card--back .brand-mark { left: 42px; top: 58px; }
  .card--back .brand-mark__name { color: var(--ink-dark); font-size: 32px; }

  .holder { position: absolute; right: 30px; top: 24px; text-align: right; }
  .holder__name { color: var(--brand-orange); font-weight: 700; font-size: 17px; }
  .holder__title { color: var(--ink-grey); font-size: 12px; }

  .cert-badge { position: absolute; right: 34px; top: 84px; width: 62px; height: 58px; border-radius: 6px; background: var(--badge-grey); }

  .website {
    position: absolute; right: 20px; top: 156px; height: 44px;
    display: flex; align-items: center;
    color: #ffffff; font-size: 12px; font-weight: 600;
    white-space: nowrap;
  }
  .contact { position: absolute; left: 30px; bottom: 20px; list-style: none; }
  .contact__item {
    display: flex; align-items: center; gap: 10px;
    color: #ffffff; font-size: 13px; line-height: 22px;
    white-space: nowrap;
  }
  .contact__icon { width: 13px; height: 13px; fill: var(--ink-dark); flex: none; }
</style>
</head>
<body>
<main class="stage">

  <section class="card card--front" aria-label="Card front">
    <div class="brand-mark">
      <span class="brand-mark__dot"></span>
      <span class="brand-mark__name">Porch &amp; Rafter<br>Check LLC</span>
    </div>
  </section>

  <section class="card card--back" aria-label="Card back">
    <svg class="card__bands" viewBox="0 0 520 300" aria-hidden="true">
      <polygon points="268,156 520,156 520,200 250,200" fill="#242424"/>
      <polygon points="0,200 300,200 262,300 0,300" fill="#e8512a"/>
    </svg>

    <div class="holder">
      <p class="holder__name">Colin Radford</p>
      <p class="holder__title">Owner/Inspector</p>
    </div>

    <div class="cert-badge" role="img" aria-label="QBRV certified badge"></div>

    <div class="brand-mark">
      <span class="brand-mark__dot"></span>
      <span class="brand-mark__name">Porch &amp; Rafter<br>Check LLC</span>
    </div>

    <p class="website">www.PorchAndRafterCheck.example</p>

    <ul class="contact">
      <li class="contact__item">
        <svg class="contact__icon" viewBox="0 0 24 24"><path d="M12 2a7 7 0 0 0-7 7c0 5 7 13 7 13s7-8 7-13a7 7 0 0 0-7-7zm0 9.5A2.5 2.5 0 1 1 12 6.5a2.5 2.5 0 0 1 0 5z"/></svg>
        WA Lic # 8467
      </li>
      <li class="contact__item">
        <svg class="contact__icon" viewBox="0 0 24 24"><path d="M6.6 10.8a15 15 0 0 0 6.6 6.6l2.2-2.2c.3-.3.7-.4 1-.2 1.1.4 2.3.6 3.6.6.6 0 1 .4 1 1V20c0 .6-.4 1-1 1A17 17 0 0 1 3 4c0-.6.4-1 1-1h3.5c.6 0 1 .4 1 1 0 1.3.2 2.5.6 3.6.1.3 0 .7-.2 1z"/></svg>
        555-718-4062
      </li>
      <li class="contact__item">
        <svg class="contact__icon" viewBox="0 0 24 24"><path d="M2 5h20v14H2zm2 2v.5l8 5 8-5V7l-8 5z"/></svg>
        ColinRadford@mailbox.example
      </li>
    </ul>
  </section>

</main>
</body>
</html>
```